One-Page Flat Design for SEO Company [2 DAYS]

We need a one-page flat design for our SEO company. Our current website is http://www.rankorchard.com/. We are looking to completely re-design the site using new flat design techniques.
Below are some examples of the type of style we're going after:
http://pelmora.com/
http://tobyharlan.co.uk/
https://quillet.co/
http://marcusfenley.me/
As you can see- flat, clean, minimal. It is very important you follow this type of style.
For colour scheme, you may use one of the pre-made colour palettes from here:
http://www.wavecrestlab.com/blog/inspiration/24-flat-designs-with-compelling-color-palettes
I've attached a wireframe to be followed.
Hi,

```html
<!DOCTYPE html>
<html lang="en">
<head>
<meta charset="utf-8">
<title>RankOrchard — SEO Services</title>
<link rel="stylesheet" href="https://fonts.googleapis.com/css2?family=Lato:wght@400;700;900&family=Open+Sans:wght@400;600;700&display=swap">
<style>
:root{
  --ink:#222;
  --nav:#1b1b1b;
  --hero-a:#1fb4e6;
  --hero-b:#3ccdf2;
  --teal:#2aae8c;
  --teal-dark:#249b7c;
  --yellow:#f5b800;
  --green:#6dbd2b;
  --green-dark:#5aa321;
  --orange:#f7941d;
  --red:#e2574c;
  --purple:#4a1d78;
  --plan-orange:#f05a28;
  --blue:#1f7bc1;
  --grey-bg:#efefef;
  --form-bg:#d6d6d6;
  --text:#666;
  --footer:#333;
}
*{box-sizing:border-box;margin:0;padding:0}
html,body{width:1200px;height:3275px;overflow:hidden}
body{position:relative;font-family:"Open Sans",Arial,sans-serif;color:var(--ink);background:#fff}
.abs{position:absolute}
.center{text-align:center;left:0;width:1200px}

/* nav */
.nav{top:0;left:0;width:1200px;height:80px;background:var(--nav)}
.logo{font-family:"Lato",sans-serif;font-weight:700;color:#fff;letter-spacing:5px}
.nav .logo{left:107px;top:18px;font-size:40px}
.nav-link{top:0;height:80px;line-height:58px;color:#fff;font-family:"Lato",sans-serif;font-weight:700;font-size:16px;letter-spacing:1px;transform:translateX(-50%)}
.nav-link.active{border-top:4px solid var(--hero-a);line-height:50px;padding:0 12px}

/* hero */
.hero{top:80px;left:0;width:1200px;height:477px;background:linear-gradient(135deg,var(--hero-a),var(--hero-b) 60%,var(--hero-a))}
.tile{color:#fff;font-family:"Open Sans",sans-serif}
.tile-main{left:110px;top:69px;width:387px;height:193px;background:var(--teal)}
.tile-main span{position:absolute;right:16px;bottom:48px;font-size:30px}
.tile-icon{left:12px;top:12px;width:90px;height:90px;border-radius:6px;background:rgba(255,255,255,.25)}
.tile-small{top:274px;width:188px;height:122px}
.tile-small span{position:absolute;bottom:10px;font-size:24px}
.tile-support{left:110px;background:var(--yellow)}
.tile-support span{right:18px}
.tile-innov{left:307px;width:190px;background:var(--green)}
.tile-innov span{right:14px}
.hero-title{left:560px;top:108px;width:530px;text-align:right;font-family:"Lato",sans-serif;font-weight:900;font-size:45px;line-height:52px;color:#fff}
.hero-sub{left:566px;top:238px;width:530px;font-size:19px;line-height:25px;color:#fff}
.btn-dark{left:884px;top:331px;width:209px;height:59px;background:#333;color:#fff;font-family:"Lato",sans-serif;font-weight:900;font-size:23px;line-height:59px;text-align:center}

/* sections */
.band-grey{left:0;width:1200px;background:var(--grey-bg)}
.section-title{font-family:"Lato",sans-serif;font-weight:900;font-size:38px;letter-spacing:1px;color:#222}
.section-sub{font-size:17px;line-height:27px;color:#555}
.service{width:240px;text-align:center}
.service-art{width:174px;height:174px;margin:0 auto}
.service h4{font-family:"Open Sans",sans-serif;font-weight:400;font-size:13px;margin-top:18px;letter-spacing:.5px}
.service p{font-size:11.5px;line-height:16px;color:#444;margin-top:12px;padding:0 18px}
.c-orange{color:var(--orange)} .bg-orange{background:var(--orange)}
.c-green{color:var(--green)} .bg-green{background:var(--green)}
.c-blue{color:var(--blue)} .bg-red{background:var(--red)}

/* plans */
.plans{top:1078px;left:0;width:1200px;height:604px;background:var(--teal)}
.plans .section-title{color:#fff}
.plans .section-sub{color:#e8fff7}
.plan{background:#f3f3f3;border:3px solid var(--teal-dark)}
.plan-head{height:84px;color:#fff;text-align:center;padding-top:14px}
.plan-head b{display:block;font-family:"Lato",sans-serif;font-weight:900;font-size:24px;letter-spacing:.5px}
.plan-head small{display:block;font-size:13px;margin-top:4px}
.plan h5{font-family:"Lato",sans-serif;font-weight:900;font-size:18px;margin:24px 0 10px 26px;letter-spacing:.5px}
.plan ul{list-style:none;margin:0 10px}
.plan li{font-size:13.5px;line-height:35px;padding-left:16px;border-top:1px solid #ddd;color:#333}
.plan .btn-go{position:absolute;left:50%;transform:translateX(-50%);bottom:20px;width:164px;height:46px;line-height:46px;background:var(--green);border-bottom:3px solid var(--green-dark);color:#fff;text-align:center;font-family:"Lato",sans-serif;font-weight:900;font-size:17px}
.plan.featured{box-shadow:0 6px 18px rgba(0,0,0,.35);border-color:#e6e6e6}
.badge{left:596px;top:1200px;width:66px;height:66px;border-radius:50%;background:var(--yellow);color:#fff;font-family:"Lato",sans-serif;font-weight:900;font-size:11px;line-height:13px;text-align:center;padding-top:20px;transform:rotate(-18deg)}

/* strip */
.strip{top:1682px;left:0;width:1200px;height:92px;background:var(--yellow)}
.strip p{position:absolute;left:160px;top:30px;font-size:25px;color:#fff}
.btn-red{left:837px;top:21px;width:193px;height:50px;background:var(--red);color:#fff;font-size:22px;line-height:50px;text-align:center}

/* contact */
.form{left:167px;top:2432px;width:869px;height:420px;background:var(--form-bg)}
.field{background:#ececec;border:1px solid #c9c9c9;color:#9a9a9a;font-size:14px;padding:12px 14px}
.btn-send{left:283px;top:358px;width:306px;height:40px;line-height:40px;background:var(--green);border-bottom:3px solid var(--green-dark);color:#fff;text-align:center;font-family:"Lato",sans-serif;font-weight:900;font-size:19px;letter-spacing:1px}
.social-link{top:2883px;font-family:"Lato",sans-serif;font-weight:900;font-size:23px;transform:translateX(-50%)}

/* footer */
.footer{top:2953px;left:0;width:1200px;height:322px;background:var(--footer)}
.footer .logo{top:45px;font-size:46px;letter-spacing:8px}
.footer p{top:107px;font-size:16px;line-height:24px;color:#eee}
.social-dot{top:176px;width:72px;height:72px;border-radius:50%;background:#141414}
</style>
</head>
<body>

<header class="nav abs">
  <div class="logo abs">LOGO</div>
  <span class="nav-link abs active" style="left:530px">HOME</span>
  <span class="nav-link abs" style="left:631px">ABOUT</span>
  <span class="nav-link abs" style="left:729px">WORK</span>
  <span class="nav-link abs" style="left:842px">SERVICES</span>
  <span class="nav-link abs" style="left:947px">TEAM</span>
  <span class="nav-link abs" style="left:1051px">CONTACT</span>
</header>

<section class="hero abs">
  <div class="tile tile-main abs">
    <div class="tile-icon abs" role="img" aria-label="Light bulb icon"></div>
    <span>Effective Solutions!</span>
  </div>
  <div class="tile tile-small tile-support abs"><span>Support</span></div>
  <div class="tile tile-small tile-innov abs"><span>Innovations</span></div>
  <h1 class="hero-title abs">FINALLY, SEO SERVICES THAT ACTUALLY WORK.</h1>
  <p class="hero-sub abs">Top-notch SEO services that are guaranteed to boost your search engine rankings. 100% Searchly-friendly.</p>
  <div class="btn-dark abs">CONTACT US</div>
</section>

<section class="band-grey abs" style="top:557px;height:521px">
  <h2 class="section-title abs center" style="top:40px">WHY CHOOSE RANKORCHARD</h2>
  <p class="section-sub abs center" style="top:98px">Fusce dapibus, tellus ac cursus commodo, tortor mauris condimentum.<br>Duis mollis, est non commodo luctus, nisi erat porttitor ligula, eget lacinia odio sem nec elit.</p>
  <div class="service abs" style="left:217px;top:196px">
    <div class="service-art bg-orange" role="img" aria-label="Branding icon: map with eye"></div>
    <h4 class="c-orange">BRANDING</h4>
    <p>This is Layerpress's version of Lorem Ipsum. Proin gravida nibh vel velit auctor aliquet. Aenean sollicitudin, lorem quis</p>
  </div>
  <div class="service abs" style="left:483px;top:196px">
    <div class="service-art bg-green" role="img" aria-label="Design icon: tablet and pen"></div>
    <h4 class="c-green">DESIGN</h4>
    <p>This is Layerpress's version of Lorem Ipsum. Proin gravida nibh vel velit auctor aliquet. Aenean sollicitudin, lorem quis</p>
  </div>
  <div class="service abs" style="left:748px;top:196px">
    <div class="service-art bg-red" role="img" aria-label="Development icon: desktop computer"></div>
    <h4 class="c-blue">DEVELOPMENT</h4>
    <p>This is Layerpress's version of Lorem Ipsum. Proin gravida nibh vel velit auctor aliquet. Aenean sollicitudin, lorem quis</p>
  </div>
</section>

<section class="plans abs">
  <h2 class="section-title abs center" style="top:30px">SELECT A BOOSTER PLAN</h2>
  <p class="section-sub abs center" style="top:82px;font-size:16px">Neque porro quisquam est, qui dolorem ipsum quia dolor sit amet</p>
</section>

<div class="plan abs" style="left:113px;top:1220px;width:250px;height:403px">
  <div class="plan-head" style="background:var(--purple)"><b>PERSONAL</b><small>$9/Month</small></div>
  <h5>FEATURES</h5>
  <ul><li>Smelly Feet</li><li>Has Bad Luck</li><li>Branding Superstar</li><li>Owns Four Cats</li><li>Vegetarian</li></ul>
  <div class="btn-go">GET STARTED</div>
</div>
<div class="plan abs" style="left:360px;top:1220px;width:244px;height:403px">
  <div class="plan-head" style="background:var(--plan-orange)"><b>PROFESSIONAL</b><small>$16/Month</small></div>
  <h5>FEATURES</h5>
  <ul><li>Mediocre Hair</li><li>Incredible UI Designer</li><li>Wrinkley Clothes</li><li>Is Moving to California</li><li>Loses at Poker</li></ul>
  <div class="btn-go">GET STARTED</div>
</div>
<div class="plan abs" style="left:851px;top:1220px;width:239px;height:403px">
  <div class="plan-head" style="background:var(--yellow)"><b>ENTERPRISE</b><small>$40/Month</small></div>
  <h5>FEATURES</h5>
  <ul><li>Smells Like Ginger</li><li>Has Four Kids</li><li>Lives in the Country</li><li>Plays Guitar Pretty Well</li><li>Great Project Pilot</li></ul>
  <div class="btn-go">GET STARTED</div>
</div>
<div class="plan featured abs" style="left:604px;top:1206px;width:247px;height:426px">
  <div class="plan-head" style="background:var(--blue)"><b>BUSINESS</b><small>$24/Month</small></div>
  <h5>FEATURES</h5>
  <ul><li>Amazing Good Looks</li><li>Handsome Hazel Eyes</li><li>Loves to Cook</li><li>Gives Great Massages</li><li>Overall Happy Dude</li></ul>
  <div class="btn-go" style="bottom:36px">GET STARTED</div>
</div>
<div class="badge abs">BEST<br>VALUE</div>

<section class="strip abs">
  <p>Duis mollis est non commodo luctus nisi erat porttitor.</p>
  <div class="btn-red abs">BUTTON</div>
</section>

<section class="band-grey abs" style="top:1774px;height:524px">
  <h2 class="section-title abs center" style="top:40px">INDIVIDUAL SEO SERVICES</h2>
  <p class="section-sub abs center" style="top:100px">usce dapibus, tellus ac cursus commodo, tortor mauris condimentum.<br>Duis mollis, est non commodo luctus, nisi erat porttitor ligula, eget lacinia odio sem nec elit.</p>
  <div class="service abs" style="left:217px;top:197px">
    <div class="service-art bg-orange" role="img" aria-label="Branding icon: map with eye"></div>
    <h4 class="c-orange">BRANDING</h4>
    <p>This is Layerpress's version of Lorem Ipsum. Proin gravida nibh vel velit auctor aliquet. Aenean sollicitudin, lorem quis</p>
  </div>
  <div class="service abs" style="left:483px;top:197px">
    <div class="service-art bg-green" role="img" aria-label="Design icon: tablet and pen"></div>
    <h4 class="c-green">DESIGN</h4>
    <p>This is Layerpress's version of Lorem Ipsum. Proin gravida nibh vel velit auctor aliquet. Aenean sollicitudin, lorem quis</p>
  </div>
  <div class="service abs" style="left:748px;top:197px">
    <div class="service-art bg-red" role="img" aria-label="Development icon: desktop computer"></div>
    <h4 class="c-blue">DEVELOPMENT</h4>
    <p>This is Layerpress's version of Lorem Ipsum. Proin gravida nibh vel velit auctor aliquet. Aenean sollicitudin, lorem quis</p>
  </div>
</section>

<section class="abs" style="top:2298px;left:0;width:1200px;height:655px">
  <h2 class="section-title abs center" style="top:24px">GET IN TOUCH</h2>
  <p class="abs center" style="top:88px;font-size:15px;color:#777">742 Alder Crest Rd, Portland, OR 97201, United States of America. Tel: (503) 555-0148</p>
</section>

<form class="form abs">
  <div class="field abs" style="left:68px;top:33px;width:355px;height:45px">Your Name</div>
  <div class="field abs" style="left:443px;top:33px;width:358px;height:45px">Your Email</div>
  <div class="field abs" style="left:68px;top:101px;width:733px;height:227px">Type your message...</div>
  <div class="btn-send abs">SEND</div>
</form>

<span class="social-link abs" style="left:389px;color:#2a5b9a">Circlebook</span>
<span class="social-link abs" style="left:530px;color:#2fb6e8">Chirpline</span>
<span class="social-link abs" style="left:657px;color:#111">Plusring</span>
<span class="social-link abs" style="left:795px;color:#1f7bc1">Linkwork</span>

<footer class="footer abs">
  <div class="logo abs center">LOGO</div>
  <p class="abs center">Fusce dapibus, tellus ac cursus commodo, tortor mauris condimentum.<br>Duis mollis, est non commodo luctus, nisi erat porttitor ligula.</p>
  <div class="social-dot abs" style="left:476px" role="img" aria-label="Social network link"></div>
  <div class="social-dot abs" style="left:559px" role="img" aria-label="Social network link"></div>
  <div class="social-dot abs" style="left:646px" role="img" aria-label="Social network link"></div>
</footer>

</body>
</html>
```